Digital Album Cover - Piano music for wedding ceremonies and receptions

I need cover art for a piano album project that will be distributed to TuneVault, Wavelane etc. Covert art required for front of album. At this stage physical CDs will not be printed nor required it is just a digital release.
Artist name: Toby Hargrove
Album Title: Gentle Keys Melodies Wedding Ceremonies and Receptions
Volume 3
Sample piano songs are on my tunecast page
https://tunecast.example/tobyhargrovekeys/sets/gentle-keys-melodies-vol-3
Previous album artwork used from sketch hive competitions winners
https://musicvault.example/au/artist/toby-hargrove/4830917265
Target Market(s)
brides to be
grooms to be
people interested in weddings
people enjoy love songs or easy listening music
Industry/Entity Type
Wedding
Look and feel
Each slider illustrates characteristics of the customer's brand and the style your logo design should communicate.

```html
<!DOCTYPE html>
<html lang="en">
<head>
<meta charset="utf-8">
<title>Toby Hargrove – Gentle Keys Melodies Volume 3</title>
<link rel="stylesheet" href="https://fonts.googleapis.com/css2?family=Raleway:wght@500;600;800&display=swap">
<style>
  :root {
    --night-deep: #0b3350;
    --night-mid: #154766;
    --moon-light: #e8f3f6;
    --moon-shade: #9fc2cf;
    --frame: #ffffff;
    --volume-number: #7b8494;
    --volume-word: #7fa5b3;
    --artist: #f4f8fa;
    --subtitle: #d3e4ea;
  }
  * { margin: 0; padding: 0; box-sizing: border-box; }
  html, body { width: 1200px; height: 1200px; overflow: hidden; background: #ffffff; }
  .album-cover {
    position: relative;
    width: 1200px;
    height: 1200px;
    overflow: hidden;
    background: radial-gradient(ellipse at 70% 60%, var(--night-mid) 0%, var(--night-deep) 75%);
    font-family: "Raleway", sans-serif;
  }
  .moon-art {
    position: absolute;
    left: -45px;
    top: -180px;
    width: 850px;
    height: 850px;
    border-radius: 50%;
    background: radial-gradient(circle at 55% 55%, var(--moon-light) 0%, #cfe3ea 45%, var(--moon-shade) 100%);
  }
  .cover-frame {
    position: absolute;
    left: 41px;
    top: 41px;
    width: 1118px;
    height: 1118px;
    border: 2px solid var(--frame);
  }
  .volume-number {
    position: absolute;
    left: 762px;
    top: 548px;
    font-size: 620px;
    font-weight: 800;
    line-height: 1;
    color: var(--volume-number);
  }
  .volume-word {
    position: absolute;
    right: 250px;
    top: 790px;
    font-size: 84px;
    font-weight: 600;
    line-height: 1;
    color: var(--volume-word);
  }
  .artist-name {
    position: absolute;
    left: 195px;
    top: 886px;
    font-size: 72px;
    font-weight: 600;
    letter-spacing: 0.14em;
    line-height: 1;
    color: var(--artist);
    white-space: nowrap;
  }
  .album-title {
    position: absolute;
    left: 197px;
    top: 984px;
    font-size: 38px;
    font-weight: 500;
    line-height: 48px;
    color: var(--subtitle);
  }
</style>
</head>
<body>
  <div class="album-cover">
    <div class="moon-art" role="img" aria-label="Photograph of a large full moon against the night sky"></div>
    <div class="volume-number">3</div>
    <div class="volume-word">Volume</div>
    <h1 class="artist-name">Toby Hargrove</h1>
    <p class="album-title">Gentle Keys Melodies Wedding<br>Ceremonies and Receptions</p>
    <div class="cover-frame"></div>
  </div>
</body>
</html>
```